Pest Control - Brolga Pest Management

Pest Control
Termites (white ants)
Cockroaches
Ants
Spiders
Bed Bugs
Rats & Mice
Bird Proofing
Termite Inspections
Termite Baiting
Pest Identification

Commercial Services
Integrated Pest Management
Scheduled Servicing
Stored Product Pest
Rodent & Bird Control

Pre - Construction
Physical Termite Barriers
Chemical Barrier Installation
Reticulation Termite Barriers

Industry/Entity Type

Construction

Contact Information for Business Card

Callum: 0417 826 391
Tess: 0419 273 845

```html
<!DOCTYPE html>
<html lang="en">
<head>
<meta charset="utf-8">
<title>Brolga Pest Management – Business Card</title>
<link rel="stylesheet" href="https://fonts.googleapis.com/css2?family=Roboto:wght@300;400;500&display=swap">
<style>
  :root {
    --page: #ffffff;
    --shadow: #bdbdbd;
    --card-dark: #1b1b1b;
    --card-mid: #2f2f2f;
    --ink: #ffffff;
    --ink-soft: #d9d9d9;
    --accent: #d8232a;
    --accent-dark: #a5161c;
    --termite-tone: #b89a63;
    --rodent-tone: #8a8680;
    --spider-tone: #6e4a3a;
    --photo-dark: #262422;
    --photo-mid: #55514b;
    --photo-light: #8c8478;
  }
  * { box-sizing: border-box; margin: 0; padding: 0; }
  html, body {
    width: 996px; height: 1200px; overflow: hidden;
    background: var(--page);
    font-family: "Roboto", Arial, sans-serif;
  }
  .sheet { position: relative; width: 996px; height: 1200px; }

  .card { position: absolute; left: 54px; width: 886px; color: var(--ink); overflow: hidden; }
  .card-front {
    top: 23px; height: 542px;
    background: repeating-linear-gradient(0deg, rgba(255,255,255,0.025) 0 1px, transparent 1px 3px),
                linear-gradient(160deg, var(--card-mid), var(--card-dark) 70%);
    box-shadow: 14px 14px 0 var(--shadow);
  }
  .card-back { top: 614px; height: 546px; }

  /* brand name */
  .brand { position: absolute; color: var(--ink); font-weight: 500; line-height: 1; }
  .brand-dot { display: inline-block; border-radius: 50%; background: var(--accent); vertical-align: top; }
  .card-front .brand { left: 52px; top: 86px; }
  .card-front .brand-name { font-size: 68px; letter-spacing: -1px; }
  .card-front .brand-sub { font-size: 44px; margin-top: 6px; }
  .card-front .brand-dot { width: 14px; height: 14px; margin: 4px 0 0 6px; }

  /* contacts */
  .contacts { position: absolute; right: 0; top: 60px; width: 420px; }
  .contact { position: relative; height: 70px; }
  .contact-name { position: absolute; right: 90px; top: 0; font-size: 22px; font-weight: 300; color: var(--ink-soft); }
  .contact-phone { position: absolute; right: 90px; top: 26px; font-size: 29px; font-weight: 400; letter-spacing: 0.5px; }
  .contact-tab {
    position: absolute; right: 0; top: 20px; width: 78px; height: 42px;
    background: linear-gradient(180deg, var(--accent), var(--accent-dark));
    display: flex; align-items: center; padding-left: 14px;
  }

  /* service lists */
  .service-list { position: absolute; left: 38px; list-style: none; font-size: 21px; font-weight: 300; }
  .service-list li { height: 27px; display: flex; align-items: center; }
  .service-list .list-head { padding-left: 35px; }
  .tick { width: 22px; height: 22px; margin-right: 13px; flex: none; }
  .list-commercial { top: 226px; }
  .list-preconstruction { top: 358px; }

  /* photo circles */
  .photo-circle { position: absolute; top: 314px; width: 144px; height: 144px; border-radius: 50%; border: 2px solid #444; }
  .photo-termites { left: 366px; background: radial-gradient(circle at 40% 40%, #d9c08c, var(--termite-tone) 55%, #6b5530); }
  .photo-rodents { left: 542px; background: radial-gradient(circle at 45% 40%, #b9b4ab, var(--rodent-tone) 55%, #4d4a45); }
  .photo-spider { left: 710px; background: radial-gradient(circle at 50% 45%, #9a7260, var(--spider-tone) 55%, #2b1e18); }
  .sectors { position: absolute; left: 374px; top: 462px; font-size: 29px; font-weight: 300; letter-spacing: 0.3px; }

  /* back */
  .back-photo {
    position: absolute; inset: 0;
    background: radial-gradient(ellipse at 30% 80%, var(--photo-light), transparent 60%),
                radial-gradient(ellipse at 75% 60%, var(--photo-mid), transparent 55%),
                linear-gradient(180deg, var(--photo-dark), #3b3833 60%, var(--photo-mid));
  }
  .back-shade { position: absolute; inset: 0; background: rgba(0,0,0,0.35); }
  .card-back .brand { left: 0; right: 0; top: 104px; text-align: center; }
  .card-back .brand-name { font-size: 40px; }
  .card-back .brand-sub { font-size: 26px; margin-top: 3px; }
  .card-back .brand-dot { width: 9px; height: 9px; margin: 2px 0 0 4px; }
  .back-services { position: absolute; left: 0; right: 0; top: 196px; text-align: center; list-style: none; font-size: 30px; font-weight: 400; line-height: 38.5px; }
</style>
</head>
<body>
<div class="sheet">

  <section class="card card-front">
    <div class="brand">
      <div class="brand-name">Brolga Pest<span class="brand-dot"></span></div>
      <div class="brand-sub">Management</div>
    </div>

    <div class="contacts">
      <div class="contact">
        <span class="contact-name">Callum</span>
        <span class="contact-phone">0417 826 391</span>
        <span class="contact-tab">
          <svg width="16" height="26" viewBox="0 0 16 26" aria-hidden="true">
            <rect x="1" y="1" width="14" height="24" rx="2" fill="none" stroke="#fff" stroke-width="2"/>
            <rect x="4" y="5" width="8" height="8" fill="#fff"/>
            <circle cx="8" cy="19" r="2" fill="#fff"/>
          </svg>
        </span>
      </div>
      <div class="contact">
        <span class="contact-name">Tess</span>
        <span class="contact-phone">0419 273 845</span>
        <span class="contact-tab">
          <svg width="16" height="26" viewBox="0 0 16 26" aria-hidden="true">
            <rect x="1" y="1" width="14" height="24" rx="2" fill="none" stroke="#fff" stroke-width="2"/>
            <rect x="4" y="5" width="8" height="8" fill="#fff"/>
            <circle cx="8" cy="19" r="2" fill="#fff"/>
          </svg>
        </span>
      </div>
    </div>

    <ul class="service-list list-commercial">
      <li class="list-head">Commercial Services</li>
      <li><svg class="tick" viewBox="0 0 22 22" aria-hidden="true"><rect x="1" y="4" width="17" height="17" fill="none" stroke="#d8232a" stroke-width="2.5"/><path d="M5 12l4 4 11-13" fill="none" stroke="#d8232a" stroke-width="3"/></svg>Integrated Pest Management</li>
      <li><svg class="tick" viewBox="0 0 22 22" aria-hidden="true"><rect x="1" y="4" width="17" height="17" fill="none" stroke="#d8232a" stroke-width="2.5"/><path d="M5 12l4 4 11-13" fill="none" stroke="#d8232a" stroke-width="3"/></svg>Scheduled Servicing</li>
      <li><svg class="tick" viewBox="0 0 22 22" aria-hidden="true"><rect x="1" y="4" width="17" height="17" fill="none" stroke="#d8232a" stroke-width="2.5"/><path d="M5 12l4 4 11-13" fill="none" stroke="#d8232a" stroke-width="3"/></svg>Stored Product Pest</li>
      <li><svg class="tick" viewBox="0 0 22 22" aria-hidden="true"><rect x="1" y="4" width="17" height="17" fill="none" stroke="#d8232a" stroke-width="2.5"/><path d="M5 12l4 4 11-13" fill="none" stroke="#d8232a" stroke-width="3"/></svg>Rodent &amp; Bird Control</li>
    </ul>

    <ul class="service-list list-preconstruction">
      <li class="list-head">Pre - Construction</li>
      <li><svg class="tick" viewBox="0 0 22 22" aria-hidden="true"><rect x="1" y="4" width="17" height="17" fill="none" stroke="#d8232a" stroke-width="2.5"/><path d="M5 12l4 4 11-13" fill="none" stroke="#d8232a" stroke-width="3"/></svg>Physical Termite Barriers</li>
      <li><svg class="tick" viewBox="0 0 22 22" aria-hidden="true"><rect x="1" y="4" width="17" height="17" fill="none" stroke="#d8232a" stroke-width="2.5"/><path d="M5 12l4 4 11-13" fill="none" stroke="#d8232a" stroke-width="3"/></svg>Chemical Barrier Installation</li>
      <li><svg class="tick" viewBox="0 0 22 22" aria-hidden="true"><rect x="1" y="4" width="17" height="17" fill="none" stroke="#d8232a" stroke-width="2.5"/><path d="M5 12l4 4 11-13" fill="none" stroke="#d8232a" stroke-width="3"/></svg>Reticulation Termite Barriers</li>
    </ul>

    <div class="photo-circle photo-termites" role="img" aria-label="Close-up photo of termites"></div>
    <div class="photo-circle photo-rodents" role="img" aria-label="Photo of mice"></div>
    <div class="photo-circle photo-spider" role="img" aria-label="Photo of a redback spider"></div>

    <p class="sectors">Residential - Commercial - Industrial</p>
  </section>

  <section class="card card-back">
    <div class="back-photo" role="img" aria-label="Dimmed full-bleed photo of mice on wood shavings"></div>
    <div class="back-shade"></div>
    <div class="brand">
      <div class="brand-name">Brolga Pest<span class="brand-dot"></span></div>
      <div class="brand-sub">Management</div>
    </div>
    <ul class="back-services">
      <li>Pest Control</li>
      <li>Termites (white ants), Cockroaches</li>
      <li>Ants, Spiders, Bed Bugs</li>
      <li>Rats &amp; Mice, Bird Proofing</li>
      <li>Termite Inspections, Termite Baiting</li>
      <li>Pest Identification</li>
    </ul>
  </section>

</div>
</body>
</html>
```